About the book: It is an A5 size book, small 40 pages miniguide
Book title: The pocket handbook of housing loans
Book subtitle: The quiet road to plenty
Author: Tod Brisbane
Back cover content: Please see attached word document "back page"
Colours: Our company logo should go at the back of the book. One colour we can't use is red. As this is a finance book the red colour is seen negatively. may be light green? you are the expert.
I think lots of white space will work well.
NOTE: please read the back cover notes to get an understanding of what the book is about. It educates readers about finance in property investing. It makes sense that image used combines 'property' and 'finance'. please read back page document attached.
NOTE: it is a small A5 , 40 page book . Its a miniguide rather than a book .
Updates

Project Deadline Extended
Reason: Dear designers, Thank you for submitting your work over the last few days. Unfortunately we haven't been able to get back to you regarding the final selection of design as the Author of the book has been away on leave with his family without reliable internet access. He is now back and will be giving feedback as we go. We apologise for the time extension. Unfortunately the site didn’t allow me to limit the extension for less than 5 days but we may not require that long. Thanks again. Lulu

Project Deadline Extended
Reason: We apologies we hadn't finalized a decision on this project due to the person from our end being away. We would like to finalise this design as soon as possible.

Target Market(s)

22 - 45 age group. Most fall between 30-40. Both male and female. couples , individuals etc ...

Industry/Entity Type

Finance

Font styles to use
Other font styles liked:
• sabon/Aeriel. Let me know if any other suggestions.

Requirements
Nice to have
• use green colour if possible but not essential.

```html
<!DOCTYPE html>
<html lang="en">
<head>
<meta charset="utf-8">
<title>The pocket handbook of housing loans — cover</title>
<link rel="stylesheet" href="https://fonts.googleapis.com/css2?family=Arimo:wght@700&display=swap">
<style>
  :root {
    --paper: #ffffff;
    --map-tone: #e9eaea;
    --map-fade: #f7f7f7;
    --globe-line: #d9dcd3;
    --band-green: #2f7d33;
    --band-green-deep: #23652a;
    --arrow-grey: #e4e4e4;
    --title-white: #ffffff;
    --subtitle-green: #2b6a2f;
  }
  html, body {
    margin: 0;
    padding: 0;
    overflow: hidden;
    background: var(--paper);
  }
  .cover {
    position: relative;
    width: 847px;
    height: 1200px;
    overflow: hidden;
    background: var(--paper);
    font-family: "Arimo", Arial, sans-serif;
  }
  .world-map {
    position: absolute;
    left: 0;
    top: 0;
    width: 847px;
    height: 760px;
    background: radial-gradient(ellipse 70% 60% at 35% 35%, var(--map-tone) 0%, var(--map-fade) 60%, var(--paper) 100%);
  }
  .globe {
    position: absolute;
    left: 420px;
    top: -70px;
    width: 500px;
    height: 500px;
    border-radius: 50%;
    background: radial-gradient(circle at 40% 45%, #fbfbf9 0%, #f1f2ee 70%, var(--globe-line) 100%);
  }
  .title-band {
    position: absolute;
    left: 0;
    top: 0;
    width: 847px;
    height: 1200px;
  }
  .title-small {
    font-size: 47px;
    font-weight: 700;
    fill: var(--title-white);
  }
  .title-large {
    font-size: 86px;
    font-weight: 700;
    fill: var(--title-white);
  }
  .subtitle {
    font-size: 50px;
    font-weight: 700;
    fill: var(--subtitle-green);
  }
</style>
</head>
<body>
<main class="cover">
  <div class="world-map" role="img" aria-label="Faint grey world map across the upper cover"></div>
  <div class="globe" role="img" aria-label="Pale wireframe globe in the top right corner"></div>

  <svg class="title-band" viewBox="0 0 847 1200" xmlns="http://www.w3.org/2000/svg">
    <defs>
      <linearGradient id="bandFill" x1="0" y1="0" x2="1" y2="0">
        <stop offset="0" stop-color="var(--band-green-deep)"/>
        <stop offset="1" stop-color="var(--band-green)"/>
      </linearGradient>
    </defs>
    <g transform="rotate(-7 0 700)">
      <polygon class="arrow" fill="var(--arrow-grey)"
               points="-40,720 700,720 700,650 800,760 700,870 700,830 -40,830"/>
      <polygon class="band" fill="url(#bandFill)"
               points="-40,530 770,530 740,725 -40,725"/>
      <text class="title-small" x="80" y="612">The pocket handbook of</text>
      <text class="title-large" x="80" y="700">housing loans</text>
      <text class="subtitle" x="80" y="800">The quiet road to plenty</text>
    </g>
  </svg>
</main>
</body>
</html>
```